new business card design - modern, professional, bold, B2B focus - with QR code pls

we are looking for a modern looking, colorful, business card design. some highlights:
- put space for QR code please. probably on the back but I'm open.
- biz card to be orientated VERTICAL not the traditional horizontal.
- do NOT use our full name on the card (ie: Allied Furnace Servicing Inc). Use only AFS Inc or AFS.
- use black and orange with some white. ideally black card with orange and white for the letters/logo etc. gray ok too - for outlines etc.
- we work in HEAVY industrial, so the cards should lend itself to this. our website is alfurnace.example, so you can see what we do.
- do NOT put in little smoke stack pictures / silouettes etc.
- think MODERN and INDUSTRIAL, with a techy focus.

Industry/Entity Type

heavy industrial - all of them. we perform maintenance and inspection services at heavy industrial and commercial businesses. so B2B

Contact Information for Business Card

name, title, phone numbers (cell + hardline), website, email address. of course our logo too - either on front or front and back.

Font styles to use
Other font styles liked:
• montserrat

Colors
F0912C
F2A743
F7CA91
FBE8D2
FDF5EE

Requirements
Must have
• see description
Nice to have
• see description
Should not have
• see description

```html
<!DOCTYPE html>
<html lang="en">
<head>
<meta charset="utf-8">
<title>AFS Inc — Business Card</title>
<link href="https://fonts.googleapis.com/css2?family=Montserrat:wght@400;500;700;800&display=swap" rel="stylesheet">
<style>
  :root{
    --backdrop:#3b3b3b;
    --card:#1c1c1c;
    --card-edge:#f0912c;
    --orange:#f39a25;
    --white:#ffffff;
    --ghost:#2b2b2b;
    --ghost-edge:#333333;
    --qr-frame:#f7ca91;
  }
  *{box-sizing:border-box;margin:0;padding:0}
  html,body{width:1200px;height:1200px;overflow:hidden}
  body{
    background:var(--backdrop);
    font-family:"Montserrat",Arial,sans-serif;
    position:relative;
  }
  .card{
    position:absolute;
    top:215px;
    width:440px;
    height:770px;
    background:var(--card);
    border-radius:36px;
    box-shadow:0 3px 0 var(--card-edge),0 18px 40px rgba(0,0,0,.45);
    overflow:hidden;
  }
  .card--back{left:120px}
  .card--front{left:640px}

  /* back: repeated wordmark with QR space */
  .wordmark-grid{
    position:absolute;inset:40px 30px;
    display:grid;
    grid-template-columns:repeat(3,1fr);
    grid-template-rows:repeat(6,1fr);
    align-items:center;justify-items:center;
  }
  .wordmark-grid span{
    font-weight:800;font-size:58px;letter-spacing:-1px;
    color:var(--ghost);
    text-shadow:0 1px 0 var(--ghost-edge);
  }
  .wordmark-grid .wordmark-grid__hero{color:var(--orange);text-shadow:none}
  .qr-space{
    width:104px;height:104px;
    background:var(--white);
    border:4px solid var(--qr-frame);
    border-radius:8px;
  }

  /* front */
  .brand{
    position:absolute;top:120px;left:0;right:0;
    text-align:center;
    font-weight:800;font-size:150px;letter-spacing:-4px;
    color:var(--orange);line-height:1;
  }
  .identity{position:absolute;left:60px;top:470px}
  .identity__name{
    font-weight:700;font-size:40px;color:var(--orange);
    line-height:1;letter-spacing:.5px;
  }
  .identity__title{
    font-weight:500;font-size:22px;color:var(--white);
    margin-top:6px;letter-spacing:.5px;
  }
  .contacts{position:absolute;left:60px;top:570px;list-style:none}
  .contacts li{
    display:flex;align-items:center;gap:16px;
    font-size:20px;color:var(--white);font-weight:500;
    height:38px;
  }
  .contacts svg{width:24px;height:24px;flex:none}
</style>
</head>
<body>

<section class="card card--back" aria-label="Card back">
  <div class="wordmark-grid">
    <span>AFS</span><span>AFS</span><span>AFS</span>
    <span>AFS</span><span>AFS</span><span>AFS</span>
    <span>AFS</span><span>AFS</span><span>AFS</span>
    <span>AFS</span><span class="wordmark-grid__hero">AFS</span><span>AFS</span>
    <span>AFS</span><span>AFS</span><span>AFS</span>
    <span>AFS</span><div class="qr-space" role="img" aria-label="Space for QR code"></div><span>AFS</span>
  </div>
</section>

<section class="card card--front" aria-label="Card front">
  <div class="brand">AFS</div>

  <div class="identity">
    <p class="identity__name">FULL NAME</p>
    <p class="identity__title">TITLE</p>
  </div>

  <ul class="contacts">
    <li>
      <svg viewBox="0 0 24 24" fill="none" stroke="var(--orange)" stroke-width="2.2"><rect x="6" y="2" width="12" height="20" rx="2"/><line x1="11" y1="18.5" x2="13" y2="18.5"/></svg>
      905-555-0173
    </li>
    <li>
      <svg viewBox="0 0 24 24" fill="var(--orange)"><path d="M6.6 10.8c1.4 2.8 3.8 5.1 6.6 6.6l2.2-2.2c.3-.3.7-.4 1-.2 1.1.4 2.3.6 3.6.6.6 0 1 .4 1 1V20c0 .6-.4 1-1 1C10.6 21 3 13.4 3 4c0-.6.4-1 1-1h3.5c.6 0 1 .4 1 1 0 1.3.2 2.5.6 3.6.1.3 0 .7-.2 1z"/></svg>
      877-555-0142
    </li>
    <li>
      <svg viewBox="0 0 24 24" fill="none" stroke="var(--orange)" stroke-width="1.8"><circle cx="12" cy="12" r="9.5"/><ellipse cx="12" cy="12" rx="4.2" ry="9.5"/><line x1="2.5" y1="12" x2="21.5" y2="12"/><path d="M4.5 7h15M4.5 17h15"/></svg>
      www.alfurnace.example
    </li>
    <li>
      <svg viewBox="0 0 24 24" fill="var(--orange)"><path d="M2 5h20v14H2z"/><path d="M2 5l10 8 10-8" fill="none" stroke="var(--card)" stroke-width="1.6"/></svg>
      afsinc@alfurnace.example
    </li>
  </ul>
</section>

</body>
</html>
```